We invest in Electric Vehicles and renewable energy - help sell us!

INTRO: We want a PowerPoint template / Master Presentation to be used to sell our company and first investment fund to professional investors and to present ourselves to businesses that will develop the infrastructure projects in which we will invest.

WHO WE ARE: We are a newly created investment advisory and fund management company specialised in sustainable mobility.

WHAT WE DO: We invest in infrastructure projects that provide electric vehicles, charging infrastructure (charging stations etc) and associated renewable energy generation services (eg solar panels on roof-tops and solar parks, wind energy). The users of the projects in which we invest are operators of vehicle fleets (taxis, buses, delivery, which may be for 2, 3 and 4 wheel vehicles from motorbikes through cars, vans, buses and trucks).

PURPOSE OF THE POWERPOINT: We are looking for a presentation (1) to sell our investment services to investors (to raise money) and (2) to present what we do to fleet operators and service providers who will develop the projects.

CONTENT: We need all of the usual front cover slide / content slide / intermediate divider-heading slide / slides that integrate the most common tables, charts and smart graphics / team slide / a variety of text slides / a testimonial slide / Example project slide / Final contact and Disclaimer text slide etc all customised to the design. We rely on your experience for providing the further standard formats and layouts that one might find in a high-quality financial sector corporate presentation deck.

VERSIONS: We want three versions of the slides where there are images (eg front and back covers, section breaks, testimonial slides..). The three could be themed eg (1) futuristic and/or abstract in the theme of our investment scope (2) Street themes with vehicles and people in developed and developing markets (3) a mix of aerial and land-based views of roads (4) more explicit around the types of infrastructure in which we invest (vehicles of different types, charging infrastructure, solar panels on industrial and commercial roof tops etc)

LOOK & FEEL: The presentation must be sleek, dynamic if sober, with a clean feel, it should project an image of clarity and confidence, but also elicit some emotional appeal (even if it is very subtle!) ... we are in the e-mobility sector after all! We have an existing logo (attached).

We have an existing website www.dorelmont.capital (one day it will need an upgrade too!) it may serve as inspiration / allow you better to understand our activities!

SOME PICS THAT WE LIKE: for inspiration only (NON exhaustive!):

• https://www.klipvane.com/video/stock/unrecognizable-highway-traffic-head-on-bgkbvhtcmjn19iqta
• https://www.klipvane.com/video/stock/new-york-city-streets-nt1vyz3
• https://www.klipvane.com/video/stock/4k-time-lapse-of-traffic-speeding-on-a-straight-section-of-highway-during-an-evening-rush-hour-ps1llt0
• https://www.klipvane.com/video/stock/cinematic-urban-aerial-time-lapse-of-city-infrastructure-including-freeways-interstates-roads-streets-with-traffic-at-rush-hour-during-the-evening-bzjhqhqfmjbhns0h9
• https://www.klipvane.com/video/stock/charging-of-electric-car-eco-energy-transport-and-power-supply-environmentally-conscious-transportation-vehicle-plugged-in-charger-terminal-in-the-city-4k-rsl8pukqmejqpaojnn
• https://www.klipvane.com/video/stock/drone-view-of-modern-vehicle-driving-on-road-near-ploughed-field-and-wind-turbine-in-countryside-rzwqrsqvdkg85gavm

FINALLY: note the attached 'slides to include' are additonal slides that we want to be well presented (see additional detail on Slide 1 of the file)

Target Market(s)

Institutional investors (pension funds, asset managers, family offices) & the dreamer in each of us!!

Industry/Entity Type

Financial services (B2B NOT B2C)

Font styles to use
Other font styles liked:
• Calibri but can consider alternatives

Requirements
Must have
• We need all of the usual front cover slide / content slide / intermediate divider-heading slide / slides that integrate the most common tables, charts and smart graphics / team slide / a variety of text slides / a testimonial slide / Example project slide / Final contact and Disclaimer text slide etc all customised to the design. We rely on your experience for providing the further standard formats and layouts that one might find in a high-quality financial sector corporate presentation deck
Nice to have
• Would like to see any other pages that are standard in your experience! Also would like to see one version of the slides with a summary section clearly marked for each slide (with space for text) which will serve for quick reading of the presentation for key points)

```html
<!DOCTYPE html>
<html lang="en">
<head>
<meta charset="utf-8">
<title>Dorelmont Capital – Slide Overview</title>
<link href="https://fonts.googleapis.com/css2?family=Roboto:wght@300;400;500;700&display=swap" rel="stylesheet">
<style>
:root{
  --green-dark:#3b5a23;
  --green-mid:#5f7d45;
  --green-soft:#7a9365;
  --green-bright:#7cb342;
  --panel:#efefef;
  --ink:#333;
  --muted:#8a8a8a;
  --rule:#e6e6e6;
  --accent-line:#f0b27a;
  --white:#fff;
}
*{margin:0;padding:0;box-sizing:border-box}
html,body{width:815px;height:1200px;overflow:hidden;background:var(--white)}
body{position:relative;font-family:'Roboto',Arial,sans-serif;color:var(--ink)}
.slide{position:absolute;width:301px;height:169px;background:var(--white);overflow:hidden;box-shadow:4px 5px 12px rgba(0,0,0,.22)}
.slide > *{position:absolute}
.col-l{left:68px}.col-r{left:436px}
.r1{top:28px}.r2{top:220px}.r3{top:412px}.r4{top:604px}.r5{top:796px}.r6{top:988px}
.brand{font-size:5.2px;font-weight:500;color:var(--green-dark);letter-spacing:.1px;white-space:nowrap}
.brand.light{color:var(--white)}
.brand-tr{right:28px;top:14px}
.title{font-size:12.5px;font-weight:300;color:var(--green-dark);white-space:nowrap;line-height:1}
.title b{font-weight:700}
.subtitle{font-size:4.6px;letter-spacing:.8px;color:#444}
.body{font-size:3.2px;line-height:6.7px;color:var(--muted);text-align:justify}
.small{font-size:3.1px;line-height:6px;color:var(--muted)}
.foot{bottom:6px;left:23px;font-size:3.2px;color:#aaa}
.page{bottom:6px;right:24px;font-size:3.2px;color:#aaa}
.photo{display:block}
.axis{font-size:3.2px;fill:#777;font-family:'Roboto',sans-serif}
.data-table{border-collapse:collapse;font-size:3px;color:var(--muted)}
.data-table th{background:var(--green-dark);color:var(--white);font-weight:700;height:9px;font-size:3.4px}
.data-table th.score{background:var(--green-mid)}
.data-table td{height:10.6px;padding-left:3px;border-bottom:.5px solid var(--rule)}
.data-table td.res{text-align:center;border-left:.5px solid var(--rule);padding:0}
.data-table.orange td{border-bottom-color:var(--accent-line)}
.data-table.orange td.res{border-left-color:var(--accent-line)}
.ring-label{font-size:6.5px;color:#444;text-anchor:middle;font-family:'Roboto',sans-serif}
.ring-sub{font-size:2.3px;fill:#999;text-anchor:middle;font-family:'Roboto',sans-serif}
.stat-head{font-size:4.2px;color:#333;text-align:center;width:60px}
.stat-body{font-size:3px;line-height:5.8px;color:var(--muted);text-align:center;width:62px}
.quote-box{background:var(--green-dark);color:var(--white);font-size:4.4px;line-height:7px;padding:9px 8px}
.check-row{display:flex;align-items:center;gap:6px;font-size:3.1px;color:var(--muted);white-space:nowrap}
.icon-circle{width:22px;height:22px;border-radius:50%;background:var(--green-dark);display:flex;align-items:center;justify-content:center}
.card{background:var(--white);box-shadow:0 1px 4px rgba(0,0,0,.15);padding:14px 0 0 7px;width:56px;height:58px}
.card h4{font-size:3.8px;font-weight:400;color:#555;margin-top:5px}
.card p{font-size:2.8px;line-height:5.6px;color:var(--muted);margin-top:4px}
.contact-band{left:0;top:112px;width:301px;height:12px;display:flex}
.contact-band .tag{width:77px;background:var(--green-bright);color:var(--white);font-size:4.4px;display:flex;align-items:center;justify-content:flex-end;padding-right:4px}
.contact-band .headline{flex:1;background:var(--green-dark);color:var(--white);font-size:6.6px;display:flex;align-items:center;padding-left:6px}
</style>
</head>
<body>

<!-- 25 Target Market: line chart -->
<section class="slide col-l r1">
  <div class="brand brand-tr">Dorelmont Capital</div>
  <svg style="left:16px;top:34px" width="148" height="98" viewBox="0 0 148 98">
    <g stroke="#ececec" stroke-width=".5">
      <line x1="12" y1="4" x2="146" y2="4"/><line x1="12" y1="15.5" x2="146" y2="15.5"/><line x1="12" y1="27" x2="146" y2="27"/>
      <line x1="12" y1="38.5" x2="146" y2="38.5"/><line x1="12" y1="50" x2="146" y2="50"/><line x1="12" y1="61.5" x2="146" y2="61.5"/>
      <line x1="12" y1="73" x2="146" y2="73"/><line x1="12" y1="84.5" x2="146" y2="84.5"/>
    </g>
    <g class="axis"><text x="2" y="5.5">70</text><text x="2" y="17">60</text><text x="2" y="28.5">50</text><text x="2" y="40">40</text><text x="2" y="51.5">30</text><text x="2" y="63">20</text><text x="2" y="74.5">10</text><text x="4" y="86">0</text>
      <text x="26" y="94">Feb</text><text x="58" y="94">Mar</text><text x="91" y="94">Apr</text><text x="124" y="94">May</text></g>
    <polyline fill="none" stroke="#2e4a1a" stroke-width=".8" points="29,33 62,8 95,67 128,64"/>
    <polyline fill="none" stroke="#3b5a23" stroke-width=".8" points="29,53 62,22 95,5 128,67"/>
    <polyline fill="none" stroke="#222" stroke-width=".7" points="29,75 62,74 95,36 128,64"/>
    <polyline fill="none" stroke="#7ed957" stroke-width=".8" points="29,51 62,53 95,67 128,72"/>
  </svg>
  <div class="title" style="left:169px;top:30px">Target <b>Market</b></div>
  <div class="subtitle" style="left:169px;top:51px">Subtitle Text</div>
  <p class="body" style="left:169px;top:62px;width:112px">Our funds back fleet operators moving to electric vehicles across growing urban markets. We finance charging hubs, depots and rooftop solar that lower running costs and emissions. Each project is screened for cash flow, grid access and partner strength before capital is committed to it, with clear reporting to investors.</p>
  <div class="foot">dorelmont.capital</div><div class="page">25</div>
</section>

<!-- 26 Target Market: rings -->
<section class="slide col-r r1">
  <div style="left:11px;top:9px;width:279px;height:150px;background:var(--panel)"></div>
  <div class="brand brand-tr">Dorelmont Capital</div>
  <div class="title" style="left:0;width:301px;text-align:center;top:32px;font-size:11.5px">Target <b>Market</b></div>
  <svg style="left:55px;top:55px" width="190" height="46" viewBox="0 0 190 46">
    <g fill="none" stroke-width="1.5">
      <circle cx="28" cy="23" r="20.5" stroke="#d6d6d6" stroke-width=".5"/>
      <path d="M28 2.5 A20.5 20.5 0 1 1 7.5 23" stroke="var(--green-bright)"/>
      <circle cx="95" cy="23" r="20.5" stroke="#d6d6d6" stroke-width=".5"/>
      <path d="M95 2.5 A20.5 20.5 0 1 1 77 13" stroke="var(--green-dark)"/>
      <circle cx="162" cy="23" r="20.5" stroke="#d6d6d6" stroke-width=".5"/>
      <path d="M162 2.5 A20.5 20.5 0 0 1 174 39.5" stroke="var(--green-mid)"/>
    </g>
    <text class="ring-label" x="28" y="23">2135</text><text class="ring-sub" x="28" y="29">Sed ut pe</text><text class="ring-sub" x="28" y="32">rspiciatis</text>
    <text class="ring-label" x="95" y="23">2245</text><text class="ring-sub" x="95" y="29">Sed ut pe</text><text class="ring-sub" x="95" y="32">rspiciatis</text>
    <text class="ring-label" x="162" y="23">1215</text><text class="ring-sub" x="162" y="29">Sed ut pe</text><text class="ring-sub" x="162" y="32">rspiciatis</text>
  </svg>
  <div class="stat-head" style="left:53px;top:112px">Your Text</div>
  <div class="stat-head" style="left:120px;top:112px">Your Text</div>
  <div class="stat-head" style="left:187px;top:112px">Your Text</div>
  <p class="stat-body" style="left:52px;top:121px">Fleet operators ready to switch to electric buses, taxis and vans.</p>
  <p class="stat-body" style="left:119px;top:121px">Fleet operators ready to switch to electric buses, taxis and vans.</p>
  <p class="stat-body" style="left:186px;top:121px">Fleet operators ready to switch to electric buses, taxis and vans.</p>
  <div class="foot">dorelmont.capital</div><div class="page">26</div>
</section>

<!-- 27 Target Market: area chart -->
<section class="slide col-l r2">
  <div class="brand brand-tr">Dorelmont Capital</div>
  <svg style="left:12px;top:40px" width="150" height="96" viewBox="0 0 150 96">
    <g stroke="#ececec" stroke-width=".5">
      <line x1="10" y1="4" x2="148" y2="4"/><line x1="10" y1="15.5" x2="148" y2="15.5"/><line x1="10" y1="27" x2="148" y2="27"/>
      <line x1="10" y1="38.5" x2="148" y2="38.5"/><line x1="10" y1="50" x2="148" y2="50"/><line x1="10" y1="61.5" x2="148" y2="61.5"/>
      <line x1="10" y1="73" x2="148" y2="73"/><line x1="10" y1="84.5" x2="148" y2="84.5"/>
    </g>
    <g class="axis"><text x="1" y="5.5">70</text><text x="1" y="17">60</text><text x="1" y="28.5">50</text><text x="1" y="40">40</text><text x="1" y="51.5">30</text><text x="1" y="63">20</text><text x="1" y="74.5">10</text><text x="3" y="86">0</text>
      <text x="10" y="93">Feb</text><text x="51" y="93">Mar</text><text x="93" y="93">Apr</text><text x="135" y="93">May</text></g>
    <polygon fill="#2e4a1a" points="12,36 55,9 96,70 140,70 140,84.5 12,84.5"/>
    <polygon fill="#5d7549" points="55,17 98,6 140,65 140,70 96,70 62,31"/>
  </svg>
  <div class="title" style="left:169px;top:30px">Target <b>Market</b></div>
  <div class="subtitle" style="left:169px;top:51px">Subtitle Text</div>
  <p class="body" style="left:169px;top:62px;width:112px">Our funds back fleet operators moving to electric vehicles across growing urban markets. We finance charging hubs, depots and rooftop solar that lower running costs and emissions. Each project is screened for cash flow, grid access and partner strength before capital is committed to it, with clear reporting to investors.</p>
  <div class="foot">dorelmont.capital</div><div class="page">27</div>
</section>

<!-- 28 Business Strategy: photo pair -->
<section class="slide col-r r2">
  <div class="brand brand-tr">Dorelmont Capital</div>
  <div class="photo" role="img" aria-label="City street canyon with yellow taxis in traffic" style="left:34px;top:24px;width:82px;height:80px;background:linear-gradient(160deg,#8e9a82,#5f6d55 55%,#b9a34a)"></div>
  <div class="photo" role="img" aria-label="Crowded market street with buses and pedestrians" style="left:97px;top:66px;width:75px;height:75px;background:linear-gradient(180deg,#6f7c7a,#8a6a55 45%,#4a4f45)"></div>
  <div class="title" style="left:203px;top:26px;line-height:15px;white-space:normal;width:90px">Business<br><b>Strategy</b></div>
  <div class="subtitle" style="left:203px;top:62px">Subtitle Text</div>
  <p class="body" style="left:203px;top:70px;width:77px;text-align:left">Our funds back fleet operators moving to electric vehicles across growing urban markets. We finance charging hubs, depots and rooftop solar that lower running costs and emissions. Each project is screened for cash flow, grid access and partner strength before capital is committed.</p>
  <div class="foot">dorelmont.capital</div><div class="page">28</div>
</section>

<!-- 29 Business Strategy: table -->
<section class="slide col-l r3">
  <div class="brand brand-tr">Dorelmont Capital</div>
  <div class="title" style="left:23px;top:20px">Business <b>Strategy</b></div>
  <div class="subtitle" style="left:23px;top:38px">Subtitle Text</div>
  <p class="body" style="left:23px;top:46px;width:252px;text-align:left">We structure long-term capital for electric fleets, charging networks and clean power, pairing patient investors with operators who run the vehicles every day across developing and developed cities. Every asset is monitored from launch through to exit.</p>
  <table class="data-table" style="left:22px;top:74px;width:167px">
    <tr><th style="width:115px">PILOT TEST</th><th class="score">100/100</th></tr>
    <tr><td>Fleet audit complete</td><td class="res">Passed</td></tr>
    <tr><td>Depot grid capacity</td><td class="res">Passed</td></tr>
    <tr><td>Charger uptime check</td><td class="res">Passed</td></tr>
    <tr><td>Route energy model</td><td class="res">Passed</td></tr>
    <tr><td>Operator credit review</td><td class="res">Passed</td></tr>
    <tr><td>Solar yield estimate</td><td class="res">Passed</td></tr>
  </table>
  <div class="quote-box" style="left:200px;top:74px;width:75px;height:75px">Just as in the digital transformation of marketing and sales, leveraging digital solutions for supply chain management requires an investment in tools and talent.</div>
  <div class="foot">dorelmont.capital</div><div class="page">29</div>
</section>

<!-- 30 Business Strategy: photo grid -->
<section class="slide col-r r3">
  <div class="brand brand-tr">Dorelmont Capital</div>
  <div class="title" style="left:23px;top:20px">Business <b>Strategy</b></div>
  <div class="subtitle" style="left:23px;top:38px">Subtitle Text</div>
  <div style="left:24px;top:52px;font-size:4.4px;color:#333">Create title here</div>
  <div style="left:182px;top:52px;font-size:4.4px;color:#333">Create title here</div>
  <p class="small" style="left:24px;top:59px;width:100px">Electric buses cut depot costs for city operators. We fund the switch with clear terms.</p>
  <p class="small" style="left:182px;top:59px;width:100px">Solar canopies power chargers by day. We pair clean energy with every hub we back.</p>
  <div role="img" aria-label="City street with taxis" style="left:2px;top:79px;width:57px;height:34px;background:linear-gradient(170deg,#7f8d72,#b3a14c)"></div>
  <div role="img" aria-label="Traffic with exhaust haze" style="left:2px;top:116px;width:57px;height:34px;background:linear-gradient(180deg,#a8a49a,#6a5a4e)"></div>
  <div style="left:62px;top:79px;width:57px;height:71px;background:var(--green-dark);color:var(--white);padding:18px 0 0 11px">
    <div style="font-size:5px;letter-spacing:.8px">Project</div>
    <div style="font-size:3px;line-height:6.2px;margin-top:5px;width:34px">Solar depot for two hundred city buses, live in year one.</div>
  </div>
  <div role="img" aria-label="Busy street with minibuses" style="left:122px;top:79px;width:57px;height:34px;background:linear-gradient(180deg,#7c8a92,#5a6052)"></div>
  <div role="img" aria-label="Crowded market road" style="left:122px;top:116px;width:57px;height:34px;background:linear-gradient(180deg,#6e7d86,#8c5e4a)"></div>
  <div role="img" aria-label="Electric bus at a stop" style="left:182px;top:79px;width:57px;height:34px;background:linear-gradient(180deg,#93b0c6,#d7dde0 50%,#6f7a60)"></div>
  <div role="img" aria-label="Minibuses in traffic" style="left:182px;top:116px;width:57px;height:34px;background:linear-gradient(180deg,#7a8a88,#b89a4a)"></div>
  <div role="img" aria-label="Highway with trucks" style="left:242px;top:79px;width:57px;height:34px;background:linear-gradient(180deg,#a9b3a4,#6c7a5e)"></div>
  <div role="img" aria-label="Aerial view of a green city" style="left:242px;top:116px;width:57px;height:34px;background:linear-gradient(180deg,#b3b9a8,#6f7d52)"></div>
  <div class="foot">dorelmont.capital</div><div class="page">30</div>
</section>

<!-- 31 Business Strategy: checks and photo strip -->
<section class="slide col-l r4">
  <div class="brand brand-tr">Dorelmont Capital</div>
  <div class="title" style="left:23px;top:20px">Business <b>Strategy</b></div>
  <div class="subtitle" style="left:23px;top:39px">Subtitle Text</div>
  <div class="check-row" style="left:21px;top:56px"><svg width="6" height="5" viewBox="0 0 6 5"><path d="M.5 2.5 2.2 4.2 5.5.8" fill="none" stroke="var(--green-dark)" stroke-width="1.2"/></svg>Clean fleets lower costs for every city operator.</div>
  <div class="check-row" style="left:21px;top:66px"><svg width="6" height="5" viewBox="0 0 6 5"><path d="M.5 2.5 2.2 4.2 5.5.8" fill="none" stroke="var(--green-dark)" stroke-width="1.2"/></svg>Charging hubs sized for daily routes.</div>
  <div class="check-row" style="left:161px;top:56px"><svg width="6" height="5" viewBox="0 0 6 5"><path d="M.5 2.5 2.2 4.2 5.5.8" fill="none" stroke="var(--green-dark)" stroke-width="1.2"/></svg>Solar supply paired with each depot we fund.</div>
  <div class="check-row" style="left:161px;top:66px"><svg width="6" height="5" viewBox="0 0 6 5"><path d="M.5 2.5 2.2 4.2 5.5.8" fill="none" stroke="var(--green-dark)" stroke-width="1.2"/></svg>Clear returns for long-term investors.</div>
  <div role="img" aria-label="Minibuses on a busy city street" style="left:0;top:84px;width:74px;height:85px;background:linear-gradient(180deg,#7d8e96,#5f7a6c 50%,#c9b457)"></div>
  <div role="img" aria-label="Charging station under a white canopy" style="left:74px;top:84px;width:153px;height:85px;background:linear-gradient(180deg,#e2dcb8,#c8c79a 40%,#7fa7a3 70%,#4d8d8a)"></div>
  <div role="img" aria-label="Zero emission electric bus" style="left:227px;top:84px;width:74px;height:85px;background:linear-gradient(180deg,#8fa866,#e5e8ea 45%,#5b7f8f)"></div>
</section>

<!-- 32 Business Strategy: cards with side photos -->
<section class="slide col-r r4">
  <div class="brand" style="left:24px;top:13px">Dorelmont Capital</div>
  <div class="title" style="left:25px;top:26px">Business <b>Strategy</b></div>
  <div class="subtitle" style="left:25px;top:44px">Subtitle Text</div>
  <div class="icon-circle" style="left:24px;top:57px"><svg width="8" height="10" viewBox="0 0 8 10"><path d="M4 .8a3 3 0 0 0-1.8 5.4V7.4h3.6V6.2A3 3 0 0 0 4 .8z" fill="none" stroke="#fff" stroke-width=".8"/><line x1="2.6" y1="8.8" x2="5.4" y2="8.8" stroke="#fff" stroke-width=".8"/></svg></div>
  <p class="small" style="left:55px;top:57px;width:82px">Electric fleets, charging hubs and solar power funded as one plan, built with local partners and run for steady yield.</p>
  <div role="img" aria-label="Crowded street with minibuses" style="left:165px;top:0;width:66px;height:169px;background:linear-gradient(180deg,#667a55,#4d6a3a 60%,#3f5a2e)"></div>
  <div role="img" aria-label="Row of city buses in traffic" style="left:236px;top:0;width:65px;height:169px;background:linear-gradient(180deg,#7c8f9a,#4c7b8e 40%,#d7c35a 65%,#5c7f8c)"></div>
  <div class="card" style="left:27px;top:90px">
    <svg width="7" height="6" viewBox="0 0 7 6"><rect x=".5" y="1.5" width="6" height="4.3" fill="var(--green-dark)"/><rect x="2.3" y=".2" width="2.4" height="1.5" fill="none" stroke="var(--green-dark)" stroke-width=".6"/></svg>
    <h4>Your Subtitle</h4><p>A clean fleet ready to roll out</p>
  </div>
  <div class="card" style="left:84px;top:90px">
    <svg width="7" height="7" viewBox="0 0 7 7"><circle cx="3.5" cy="3.5" r="3" fill="none" stroke="var(--green-dark)" stroke-width=".8"/><circle cx="3.5" cy="3.5" r="1.1" fill="var(--green-dark)"/></svg>
    <h4>Your Subtitle</h4><p>A clean fleet ready to roll out</p>
  </div>
  <div class="card" style="left:141px;top:90px">
    <svg width="7" height="6" viewBox="0 0 7 6"><path d="M.4.3V5.6H6.8" fill="none" stroke="var(--green-bright)" stroke-width=".6"/><path d="M1.3 4.5 3 2.6 4.2 3.6 6.4 1.2" fill="none" stroke="var(--green-bright)" stroke-width=".7"/></svg>
    <h4>Your Subtitle</h4><p>A clean fleet ready to roll out</p>
  </div>
  <div class="foot">dorelmont.capital</div>
</section>

<!-- 33 Business Strategy: icon rows with traffic photo -->
<section class="slide col-l r5">
  <div class="brand" style="left:24px;top:13px">Dorelmont Capital</div>
  <div role="img" aria-label="Traffic in smoky haze" style="left:150px;top:0;width:151px;height:169px;background:linear-gradient(180deg,#a7ada2,#8a8f86 50%,#6d7468)"></div>
  <div style="left:220px;top:0;width:81px;height:169px;background:linear-gradient(180deg,rgba(74,110,50,.78),rgba(96,130,70,.7))"></div>
  <div class="brand light" style="left:240px;top:13px">Dorelmont Capital</div>
  <div class="title" style="left:23px;top:40px">Business <b>Strategy</b></div>
  <div class="subtitle" style="left:23px;top:59px">Subtitle Text</div>
  <div class="icon-circle" style="left:25px;top:78px"><svg width="10" height="10" viewBox="0 0 10 10"><path d="M5 1.2 7.6 5.6H2.4z" fill="none" stroke="#fff" stroke-width=".8"/><circle cx="5" cy="7.8" r="1" fill="#fff"/></svg></div>
  <p class="small" style="left:58px;top:77px;width:82px">We finance electric buses and taxis for city fleets, cutting fuel bills and local pollution while returns stay steady for investors.</p>
  <div class="icon-circle" style="left:25px;top:116px"><svg width="11" height="7" viewBox="0 0 11 7"><path d="M1 5V3.2L2.6 1h5.6L10 3.2V5z" fill="none" stroke="#fff" stroke-width=".8"/><circle cx="3" cy="5.6" r=".9" fill="#fff"/><circle cx="8" cy="5.6" r=".9" fill="#fff"/></svg></div>
  <p class="small" style="left:58px;top:115px;width:82px">Charging sites are placed where fleets park each night, so vehicles leave full and routes run on time with no wasted miles.</p>
  <div class="foot">dorelmont.capital</div>
</section>

<!-- 34 Business Strategy: angled photo panel -->
<section class="slide col-r r5">
  <svg role="img" aria-label="Electric car charging port and charger close-ups" style="left:120px;top:0" width="181" height="169" viewBox="0 0 181 169">
    <defs><linearGradient id="evTone" x1="0" y1="0" x2="1" y2="1"><stop offset="0" stop-color="#9fb0a4"/><stop offset=".45" stop-color="#c9d2de"/><stop offset=".7" stop-color="#3f56b8"/><stop offset="1" stop-color="#6a7d66"/></linearGradient></defs>
    <polygon points="80,0 181,0 181,169 0,169 75,90 60,40" fill="url(#evTone)"/>
    <polygon points="130,0 181,0 181,40" fill="var(--green-dark)"/>
    <polygon points="181,95 181,169 145,169" fill="var(--green-dark)"/>
    <g stroke="#fff" stroke-width="3"><line x1="60" y1="40" x2="181" y2="160"/><line x1="170" y1="0" x2="20" y2="169"/><line x1="100" y1="0" x2="181" y2="80"/></g>
  </svg>
  <div class="title" style="left:23px;top:40px">Business <b>Strategy</b></div>
  <div class="subtitle" style="left:23px;top:59px">Subtitle Text</div>
  <div class="icon-circle" style="left:24px;top:72px"><svg width="8" height="10" viewBox="0 0 8 10"><path d="M4 .8a3 3 0 0 0-1.8 5.4V7.4h3.6V6.2A3 3 0 0 0 4 .8z" fill="none" stroke="#fff" stroke-width=".8"/><line x1="2.6" y1="8.8" x2="5.4" y2="8.8" stroke="#fff" stroke-width=".8"/></svg></div>
  <p class="small" style="left:55px;top:72px;width:82px">Electric fleets, charging hubs and solar power funded as one plan, built with local partners and run for steady yield.</p>
  <div class="check-row" style="left:30px;top:109px;align-items:flex-start"><svg width="6" height="5" viewBox="0 0 6 5"><path d="M.5 2.5 2.2 4.2 5.5.8" fill="none" stroke="var(--green-dark)" stroke-width="1.2"/></svg><span style="white-space:normal;width:60px;line-height:6px">Fast chargers at depots keep each fleet moving every day.</span></div>
  <div class="check-row" style="left:30px;top:129px;align-items:flex-start"><svg width="6" height="5" viewBox="0 0 6 5"><path d="M.5 2.5 2.2 4.2 5.5.8" fill="none" stroke="var(--green-dark)" stroke-width="1.2"/></svg><span style="white-space:normal;width:60px;line-height:6px">Clean power lowers the cost of every trip for operators.</span></div>
  <div class="foot">dorelmont.capital</div>
</section>

<!-- 35 Our Services -->
<section class="slide col-l r6">
  <div role="img" aria-label="Charging station under solar canopy" style="left:200px;top:0;width:101px;height:169px;background:linear-gradient(180deg,#c7c88f,#a3b27a 40%,#6f9a7c 75%,#4e8a6c)"></div>
  <div class="brand light" style="left:240px;top:13px">Dorelmont Capital</div>
  <div class="title" style="left:22px;top:20px">Our <b>Services</b></div>
  <p class="body" style="left:22px;top:37px;width:170px;text-align:left">We structure long-term capital for electric fleets, charging networks and clean power, pairing patient investors with operators who run the vehicles every day across developing and developed cities and regions.</p>
  <table class="data-table orange" style="left:22px;top:74px;width:168px">
    <tr><th style="width:116px">Training Services</th><th>Result</th></tr>
    <tr><td>Fleet audit complete</td><td class="res">Passed</td></tr>
    <tr><td>Depot grid capacity</td><td class="res">Passed</td></tr>
    <tr><td>Charger uptime check</td><td class="res">Passed</td></tr>
    <tr><td>Route energy model</td><td class="res">Passed</td></tr>
    <tr><td>Operator credit review</td><td class="res">Passed</td></tr>
    <tr><td>Solar yield estimate</td><td class="res">Passed</td></tr>
  </table>
  <div class="foot">dorelmont.capital</div>
</section>

<!-- 36 Contact -->
<section class="slide col-r r6">
  <div role="img" aria-label="Hand holding a smartphone above a laptop" style="left:0;top:0;width:301px;height:112px;background:linear-gradient(120deg,#8a8f9c,#6b6470 45%,#b7927e 75%,#d8c4b4)"></div>
  <div class="brand light" style="left:42px;top:82px;font-size:13px;font-weight:300">Dorelmont Capital</div>
  <div class="contact-band"><div class="tag">Contact Us</div><div class="headline">Keep &nbsp;in Touch</div></div>
  <svg style="left:80px;top:137px" width="10" height="14" viewBox="0 0 10 14"><path d="M5 .5a4.5 4.5 0 0 0-4.5 4.5C.5 8.5 5 13.5 5 13.5S9.5 8.5 9.5 5A4.5 4.5 0 0 0 5 .5z" fill="var(--green-dark)"/><circle cx="5" cy="5" r="1.7" fill="#fff"/></svg>
  <p class="small" style="left:98px;top:136px;width:72px">Suite 2, Harlow House,<br>Fenwick Road, Westbay,<br>Coastal District.</p>
  <svg style="left:201px;top:132px" width="6" height="5" viewBox="0 0 6 5"><rect x=".4" y=".4" width="5.2" height="4.2" fill="none" stroke="var(--green-dark)" stroke-width=".6"/><path d="M.4.4 3 2.6 5.6.4" fill="none" stroke="var(--green-dark)" stroke-width=".6"/></svg>
  <div class="small" style="left:213px;top:131px">info@dorelmont.capital</div>
  <svg style="left:201px;top:141px" width="6" height="6" viewBox="0 0 6 6"><path d="M1 .5 2.3 1.8 1.6 2.6Q2.6 4 3.4 4.4L4.2 3.7 5.5 5 4.6 5.7Q1.8 5 .3 1.4z" fill="var(--green-dark)"/></svg>
  <div class="small" style="left:211px;top:140px">+001 5550142</div>
  <svg style="left:201px;top:150px" width="6" height="5" viewBox="0 0 6 5"><rect x=".8" y=".4" width="4.4" height="3" fill="none" stroke="var(--green-dark)" stroke-width=".6"/><line x1=".2" y1="4.4" x2="5.8" y2="4.4" stroke="var(--green-dark)" stroke-width=".6"/></svg>
  <div class="small" style="left:209px;top:149px">www.dorelmont.capital</div>
  <div class="foot">dorelmont.capital</div><div class="page">36</div>
</section>

</body>
</html>
```